Designing a website that functions as the shop window for the various aspects of my business -...

I need a website, with separate webpages covering the different components of my practice (small animal consultancy, equine behaviour consultancy, legal case work and education provider). I have a website (www.petmindstudio-example.ie) but I haven't updated it in recent years to reflect the newer developments / aspects of my business. Most of my work has been in Ireland but I would like to begin to create an international profile, particularly with regard to the legal casework and offering education within the international horse industry. My overall goal is to improve understanding of animals and animal behaviour, and by doing so, help to reduce the performance of behaviour problems, and also improve animal welfare as a result.

Target Market(s)

Horse and dog owners, horse riders, veterinary surgeons, solicitors

Industry/Entity Type

Legal

Logo Text

Text to be decided on

Number of Pages Required

5+ page

Font styles to use
Sans Serif
Decorative
Script

Colors

Designer to choose colors to be used in the design.

Requirements
Must have
• Relevant content from the attached Flyer including photos
• Use of the phrases:
• 'Understanding Animals'
• Improving animals lives through better understanding
• Science-based, up-to-date relevant information regarding animal behaviour
Nice to have
• 'Leading professional service educating people in understanding animals'
• Separate pages for 1) About, 2) Canine and Feline behaviour Consultancy 3) Equine Consultancy 4) Legal expert witness Consultancy 5) Education 6, FAQs
Should not have
• Prices of services (as these may change from time to time)

```html
<!DOCTYPE html>
<html lang="en">
<head>
<meta charset="utf-8">
<title>PetMind Studio</title>
<link href="https://fonts.googleapis.com/css2?family=Open+Sans:wght@400;600;700;800&family=Courgette&display=swap" rel="stylesheet">
<style>
:root{
  --green:#128148;
  --green-dark:#0d6a3a;
  --ink:#222;
  --muted:#666;
  --dark:#2b2b2b;
  --white:#fff;
  --ghost:#e9e9e9;
}
*{box-sizing:border-box;margin:0;padding:0}
html,body{width:1200px;height:3509px;overflow:hidden}
body{position:relative;background:var(--white);font-family:"Open Sans",sans-serif;color:var(--ink)}
.abs{position:absolute}
.script{font-family:"Courgette",cursive}

/* header */
.header-hours{left:130px;top:26px;text-align:right;width:188px;font-size:15px;line-height:19px}
.header-hours b{font-size:18px;display:block}
.round-icon{width:42px;height:42px;border:2px solid var(--green);border-radius:50%;display:flex;align-items:center;justify-content:center}
.brand{left:488px;top:30px;font-size:30px;color:var(--green);font-weight:700;letter-spacing:.5px}
.header-call{left:830px;top:26px;width:162px;text-align:right;font-size:15px;line-height:19px}
.header-call b{font-size:22px;display:block}

.nav{left:0;top:105px;width:1200px;height:42px;background:var(--green);display:flex;padding-left:145px}
.nav a{color:var(--white);text-decoration:none;font-size:12.5px;font-weight:600;line-height:42px;padding:0 12px}
.nav a.active{background:#222}

/* hero */
.hero{left:0;top:147px;width:1200px;height:625px;background:linear-gradient(100deg,#7d7a4c 0%,#9aa45a 35%,#6f8c3a 60%,#c59c3a 100%)}
.hero-photo{left:140px;top:147px;width:380px;height:520px;background:radial-gradient(ellipse at center,#eee9df 0%,#d9d2c2 55%,rgba(217,210,194,0) 72%)}
.hero-title{left:640px;top:245px;font-size:88px;line-height:100px;color:var(--white);text-shadow:0 2px 6px rgba(0,0,0,.35)}
.arrow-btn{width:36px;height:36px;border-radius:50%;background:#2a2a2a;color:#fff;display:flex;align-items:center;justify-content:center;font-size:16px}

.feature{width:292px;height:292px;border-radius:50%;background:var(--white);border-top:6px solid var(--green);box-shadow:0 4px 14px rgba(0,0,0,.12);text-align:center;padding-top:40px}
.feature .icon{width:74px;height:74px;margin:0 auto 14px;border-radius:50%;background:#e8f2ec;border:2px solid #333}
.feature h3{font-size:17.5px;font-weight:700;line-height:22px;padding:0 40px}
.feature p{font-size:11.5px;color:var(--muted);line-height:17px;padding:6px 58px 0}
.btn-outline{display:inline-block;margin-top:18px;border:2px solid var(--green);border-radius:22px;padding:8px 18px;font-size:11.5px;font-weight:700;color:var(--green)}

/* welcome */
.ghost{font-weight:800;color:var(--ghost);letter-spacing:4px}
.welcome-brand{left:390px;top:1014px;width:420px;text-align:center;font-size:36px;color:var(--green);font-weight:700}
.intro{left:215px;top:1112px;width:770px;text-align:center;font-size:13px;line-height:32.5px;color:var(--muted)}
.video{left:276px;top:1287px;width:648px;height:346px;background:linear-gradient(90deg,#4a4a3c,#6d7a45 50%,#4f6a2e);z-index:2}
.play{left:567px;top:1428px;width:66px;height:66px;border-radius:50%;background:#e11;z-index:3;display:flex;align-items:center;justify-content:center}

.offer-band{left:0;top:1546px;width:1200px;height:520px;background:var(--green)}
.offer-ghost{left:0;top:1650px;font-size:96px;color:rgba(0,0,0,.1);font-weight:800}
.section-title{font-size:40px;text-align:center;width:1200px;left:0}
.offer-item{width:240px;text-align:center;color:var(--white)}
.offer-item .ring{width:117px;height:117px;margin:0 auto;border:3px solid var(--white);border-radius:50%;display:flex;align-items:center;justify-content:center}
.offer-item .ring span{width:70px;height:70px;border-radius:50%;background:rgba(255,255,255,.25)}
.offer-item h4{font-size:18.5px;font-weight:400;line-height:23px;margin-top:14px}

/* components */
.dark-band{left:0;top:2526px;width:1200px;height:702px;background:var(--dark)}
.comp-box{left:110px;top:2260px;width:980px;height:332px;background:var(--white)}
.comp{width:215px;text-align:center}
.comp .photo{height:201px}
.comp h4{font-size:17px;font-weight:700;line-height:22px;margin-top:18px}
.comp h4.on{color:var(--green)}

/* contact */
.field{background:var(--white);font-size:13.5px;color:#555;padding:14px 20px}
.btn-submit{left:494px;top:3078px;width:210px;height:48px;border-radius:24px;background:var(--green);color:var(--white);font-weight:700;font-size:16px;display:flex;align-items:center;justify-content:center}

/* footer */
.social{width:52px;height:52px;border:1.5px solid #ccc;border-radius:50%}
.foot-nav{left:0;top:3371px;width:1200px;text-align:center;font-size:13px;font-weight:600}
.foot-contact{left:0;top:3411px;width:1200px;text-align:center;font-size:13px;color:var(--muted)}
.foot-copy{left:0;top:3449px;width:1200px;text-align:center;font-size:12.5px;color:var(--muted)}
.foot-contact svg{vertical-align:-2px;margin-right:4px}
</style>
</head>
<body>

<header>
  <div class="abs header-hours">Mon-Fri<b>9.30 am until 6.00pm</b></div>
  <div class="abs round-icon" style="left:332px;top:25px">
    <svg width="22" height="22" viewBox="0 0 24 24" fill="none" stroke="#128148" stroke-width="2"><circle cx="12" cy="12" r="9"/><path d="M12 7v5l3 2"/></svg>
  </div>
  <div class="abs brand">PetMind Studio</div>
  <div class="abs header-call">Call Us :<b>087 555 0142</b></div>
  <div class="abs round-icon" style="left:1007px;top:25px">
    <svg width="20" height="20" viewBox="0 0 24 24" fill="#128148"><path d="M6.6 10.8a15 15 0 006.6 6.6l2.2-2.2a1 1 0 011-.25 11.4 11.4 0 003.6.6 1 1 0 011 1V20a1 1 0 01-1 1A17 17 0 013 4a1 1 0 011-1h3.5a1 1 0 011 1 11.4 11.4 0 00.6 3.6 1 1 0 01-.25 1z"/></svg>
  </div>
  <nav class="abs nav">
    <a class="active">HOME</a><a>ABOUT</a><a>CANINE AND FELINE BEHAVIOUR CONSULTANCY</a><a>EQUINE CONSULTANCY</a><a>LEGAL EXPERT WITNESS CONSULTANCY</a><a>MORE..</a>
  </nav>
</header>

<section>
  <div class="abs hero" role="img" aria-label="Photo of a small white terrier lying on grass in sunlight"></div>
  <div class="abs hero-photo" role="img" aria-label="Terrier in foreground"></div>
  <div class="abs arrow-btn" style="left:32px;top:378px">&larr;</div>
  <div class="abs arrow-btn" style="left:32px;top:426px">&rarr;</div>
  <h1 class="abs hero-title script">PetMind<br>Studio</h1>

  <div class="abs feature" style="left:144px;top:627px">
    <div class="icon" role="img" aria-label="Cat icon"></div>
    <h3>Improving animals lives through better understanding</h3>
    <span class="btn-outline">READ MORE &#10148;</span>
  </div>
  <div class="abs feature" style="left:455px;top:632px">
    <div class="icon" role="img" aria-label="Dog icon"></div>
    <h3>Understanding Animals</h3>
    <p>Lorem ipsum dolor sit amet, consectetur adipiscing elo eiusmod tempor</p>
    <span class="btn-outline" style="margin-top:12px">READ MORE &#10148;</span>
  </div>
  <div class="abs feature" style="left:764px;top:627px">
    <div class="icon" role="img" aria-label="Brain icon"></div>
    <h3>Science-based, up-to-date relevant information regarding animal behaviour</h3>
    <span class="btn-outline" style="margin-top:12px">READ MORE &#10148;</span>
  </div>
</section>

<section>
  <div class="abs ghost" style="left:850px;top:972px;font-size:92px">WELCO</div>
  <div class="abs welcome-brand">PetMind Studio</div>
  <p class="abs intro">Animals have been used by humans for a variety of purposes, including as a source of food, for hunting, for mobility, to help win battles, for sport - and most recently, for companionship. Whether we are dog or cat lovers, horseriders or owners, through the course of our relationship with our animals, many of us will be faced with problem behaviours, such as aggression, excessive barking, destructiveness (dogs), spraying, fear problems, aggression (cats), bucking, refusing to load into trailers, rearing, shying (horses).</p>
  <div class="abs offer-band"></div>
  <div class="abs video" role="img" aria-label="Video still of a dog beside grazing horses"></div>
  <div class="abs play"><svg width="26" height="28" viewBox="0 0 26 28"><path d="M3 2l21 12L3 26z" fill="#fff"/></svg></div>
</section>

<section>
  <div class="abs offer-ghost">WE OFFER</div>
  <h2 class="abs section-title script" style="top:1690px;color:var(--white)">What we offer</h2>
  <div class="abs offer-item" style="left:95px;top:1797px"><div class="ring" role="img" aria-label="Person icon"><span></span></div><h4>Behaviour<br>consultations</h4></div>
  <div class="abs offer-item" style="left:310px;top:1797px"><div class="ring" role="img" aria-label="Person walking dog icon"><span></span></div><h4>Training<br>sessions</h4></div>
  <div class="abs offer-item" style="left:554px;top:1797px"><div class="ring" role="img" aria-label="Horse icon"><span></span></div><h4>Training your horse -<br>theory and practice</h4></div>
  <div class="abs offer-item" style="left:827px;top:1797px"><div class="ring" role="img" aria-label="Person training dog icon"><span></span></div><h4>Training, performance<br>and welfare</h4></div>
</section>

<section>
  <div class="abs ghost" style="left:0;width:1200px;text-align:center;top:2150px;font-size:96px">COMPONENTS</div>
  <h2 class="abs section-title script" style="top:2193px;color:var(--ink)">Our Components</h2>
  <div class="abs dark-band"></div>
  <div class="abs comp-box"></div>
  <div class="abs comp" style="left:143px;top:2297px"><div class="photo" role="img" aria-label="Dog on grass" style="background:linear-gradient(135deg,#3d4a2a,#6f7d4a)"></div><h4>SMALL ANIMAL<br>CONSULTANCY</h4></div>
  <div class="abs comp" style="left:374px;top:2297px"><div class="photo" role="img" aria-label="Business handshake" style="background:linear-gradient(135deg,#3a3a3a,#b9b9b9)"></div><h4 class="on">EQUINE BEHAVIOUR<br>CONSULTANCY</h4></div>
  <div class="abs comp" style="left:608px;top:2297px"><div class="photo" role="img" aria-label="Glasses on documents" style="background:linear-gradient(135deg,#2a2a2a,#d9d9d9)"></div><h4>LEGAL CASE WORK</h4></div>
  <div class="abs comp" style="left:840px;top:2297px"><div class="photo" role="img" aria-label="Students seated together" style="background:linear-gradient(135deg,#d8c7b0,#5b4a3e)"></div><h4>EDUCATION PROVIDER</h4></div>
</section>

<section>
  <div class="abs" style="left:0;width:1200px;text-align:center;top:2680px;font-size:96px;font-weight:800;color:rgba(255,255,255,.07);letter-spacing:4px">CONTACT US</div>
  <h2 class="abs section-title script" style="top:2722px;color:var(--white)">Contact form</h2>
  <div class="abs field" style="left:215px;top:2821px;width:374px;height:45px">First Name</div>
  <div class="abs field" style="left:610px;top:2821px;width:375px;height:45px">Last Name</div>
  <div class="abs field" style="left:215px;top:2889px;width:374px;height:47px">Email Address</div>
  <div class="abs field" style="left:610px;top:2889px;width:375px;height:47px">Phone</div>
  <div class="abs field" style="left:215px;top:2957px;width:770px;height:84px">Message</div>
  <div class="abs btn-submit">SUBMIT MESSAGE</div>
</section>

<footer>
  <div class="abs social" style="left:478px;top:3286px" role="img" aria-label="Social link"></div>
  <div class="abs social" style="left:542px;top:3286px" role="img" aria-label="Social link"></div>
  <div class="abs social" style="left:606px;top:3286px" role="img" aria-label="Social link"></div>
  <div class="abs social" style="left:670px;top:3286px" role="img" aria-label="Social link"></div>
  <div class="abs foot-nav">HOME &nbsp;/&nbsp; ABOUT &nbsp;/&nbsp; CANINE &amp; FELINE BEHAVIOUR CONSULTANCY &nbsp;/&nbsp; EQUINE CONSULTANCY &nbsp;/&nbsp; LEGAL EXPERT WITNESS CONSULTANCY &nbsp;/&nbsp; MORE..</div>
  <div class="abs foot-contact">
    <svg width="11" height="14" viewBox="0 0 12 16" fill="#128148"><path d="M6 0a6 6 0 00-6 6c0 4.5 6 10 6 10s6-5.5 6-10a6 6 0 00-6-6zm0 8.5A2.5 2.5 0 116 3.5a2.5 2.5 0 010 5z"/></svg>734,Lorem ipsum dolor sadipiscing &nbsp;|&nbsp;
    <svg width="13" height="13" viewBox="0 0 24 24" fill="#128148"><path d="M6.6 10.8a15 15 0 006.6 6.6l2.2-2.2a1 1 0 011-.25 11.4 11.4 0 003.6.6 1 1 0 011 1V20a1 1 0 01-1 1A17 17 0 013 4a1 1 0 011-1h3.5a1 1 0 011 1 11.4 11.4 0 00.6 3.6 1 1 0 01-.25 1z"/></svg>087 555 0142 &nbsp;|&nbsp;
    <svg width="15" height="12" viewBox="0 0 20 14" fill="#128148"><path d="M0 0h20v14H0z"/><path d="M0 0l10 7 10-7" stroke="#fff" stroke-width="1.5" fill="none"/></svg>hello@petmindstudio-example.ie
  </div>
  <div class="abs foot-copy">&copy; 2019 Copyrights.Companyname.All Rights Reserved</div>
</footer>

</body>
</html>
```